Night Dresses business cards business requirers

We are a new company initiating Mexico operations. Our core business is Night woman dress (both formal and party dress) for rent. Gownhaven is the name of the company. ITS Gownhaven form by two word. The dress word and topia (Utopic) so the place Gownhaven Means That You cant get the ideal, perfect and unique dress for your event. So we would like a modern, very creative, and attractive business card.

Industry/Entity Type

Womens Clothing

Contact Information for Business Card

Rounded Borders, two faces

Requirements
Must have
• Rounded borders, logo and slogan, modern, glam, attractive design
Should not have
• modern design classic or not

```html
<!DOCTYPE html>
<html lang="en">
<head>
<meta charset="utf-8">
<title>Gownhaven — Business Cards</title>
<link rel="stylesheet" href="https://fonts.googleapis.com/css2?family=Montserrat:wght@500;600&family=Crimson+Text:wght@400&family=Allura&display=swap">
<style>
  :root {
    --canvas-bg: #e6e7e9;
    --card-white: #f7f7f8;
    --card-white-shade: #e9e9ec;
    --brand-pink: #b8468f;
    --brand-pink-light: #d46aac;
    --brand-pink-deep: #a83c83;
    --ink-dark: #3a3a3c;
    --ink-light: #ffffff;
    --ornament-pink: #b04a8c;
    --ornament-white: #f4dcea;
  }
  * { box-sizing: border-box; margin: 0; padding: 0; }
  html, body {
    width: 1200px; height: 1200px; overflow: hidden;
    background: var(--canvas-bg);
  }
  .sheet {
    position: relative; width: 1200px; height: 1200px;
    display: flex; flex-direction: column; align-items: center; justify-content: center;
    gap: 80px;
  }
  .card {
    position: relative; width: 840px; height: 480px;
    border-radius: 22px; overflow: hidden;
    box-shadow: 0 6px 18px rgba(0,0,0,0.12);
  }
  .card-front {
    background: radial-gradient(ellipse at 45% 45%, var(--card-white) 30%, var(--card-white-shade) 100%);
  }
  .card-back {
    background: linear-gradient(120deg, var(--brand-pink-deep) 0%, var(--brand-pink) 45%, var(--brand-pink-light) 100%);
  }
  .floral-texture { position: absolute; inset: 0; }
  .card-front .floral-texture {
    background: radial-gradient(circle at 25% 75%, rgba(255,255,255,0.6), transparent 40%),
                radial-gradient(circle at 80% 25%, rgba(255,255,255,0.5), transparent 35%);
  }
  .card-back .floral-texture {
    background: radial-gradient(circle at 30% 30%, rgba(150,40,110,0.25), transparent 40%),
                radial-gradient(circle at 75% 80%, rgba(150,40,110,0.2), transparent 40%);
  }
  .frame { position: absolute; inset: 30px; border: 1.5px solid; }
  .card-front .frame { border-color: var(--brand-pink); }
  .card-back .frame { border-color: rgba(255,255,255,0.85); }
  .corner { position: absolute; width: 62px; height: 62px; border-radius: 6px; }
  .card-front .corner { background: var(--ornament-pink); opacity: 0.85; }
  .card-back .corner { background: var(--ornament-white); opacity: 0.9; }
  .corner.tl { top: 16px; left: 16px; }
  .corner.tr { top: 16px; right: 16px; }
  .corner.bl { bottom: 16px; left: 16px; }
  .corner.br { bottom: 16px; right: 16px; }

  .brand {
    position: absolute; top: 50%; left: 50%; transform: translate(-50%, -50%);
    display: flex; flex-direction: column; align-items: center; gap: 10px;
    white-space: nowrap;
  }
  .brand-name {
    font-family: "Montserrat", sans-serif; font-weight: 600;
    font-size: 44px; letter-spacing: 10px; color: var(--ink-dark);
  }
  .brand-slogan {
    font-family: "Montserrat", sans-serif; font-weight: 600;
    font-size: 17px; letter-spacing: 6px; color: var(--ink-dark);
  }

  .contact-block {
    position: absolute; top: 96px; left: 160px; width: 520px;
    text-align: center; color: var(--ink-light);
    font-family: "Crimson Text", serif;
  }
  .person-name { font-family: "Allura", cursive; font-size: 72px; line-height: 1; }
  .person-title { font-size: 24px; margin-top: 2px; }
  .divider {
    width: 100%; height: 1.5px; background: rgba(255,255,255,0.9);
    margin: 22px 0 20px;
  }
  .contact-line { font-size: 23px; line-height: 1.5; }
</style>
</head>
<body>
<main class="sheet">
  <section class="card card-front">
    <div class="floral-texture" role="img" aria-label="Faint white floral pattern background"></div>
    <div class="frame"></div>
    <div class="corner tl" role="img" aria-label="Pink filigree corner ornament"></div>
    <div class="corner tr" role="img" aria-label="Pink filigree corner ornament"></div>
    <div class="corner bl" role="img" aria-label="Pink filigree corner ornament"></div>
    <div class="corner br" role="img" aria-label="Pink filigree corner ornament"></div>
    <div class="brand">
      <span class="brand-name">GOWNHAVEN</span>
      <span class="brand-slogan">EVENING WEAR RENTALS</span>
    </div>
  </section>

  <section class="card card-back">
    <div class="floral-texture" role="img" aria-label="Tone-on-tone pink floral pattern background"></div>
    <div class="frame"></div>
    <div class="corner tl" role="img" aria-label="White filigree corner ornament"></div>
    <div class="corner tr" role="img" aria-label="White filigree corner ornament"></div>
    <div class="corner bl" role="img" aria-label="White filigree corner ornament"></div>
    <div class="corner br" role="img" aria-label="White filigree corner ornament"></div>
    <div class="contact-block">
      <p class="person-name">Elena Ruiz</p>
      <p class="person-title">Director</p>
      <div class="divider"></div>
      <p class="contact-line">1-555-014-2290</p>
      <p class="contact-line">Calle Olmo 12, Villa Serena</p>
      <p class="contact-line">www.gownhaven.com | elena@gownhaven.com</p>
    </div>
  </section>
</main>
</body>
</html>
```